Powerpoint template & style design project

KMaldrey Consulting is an IT technology firm specializing in mobility and telecommunications applications. We provide technical consulting to global companies that want to build mobile applications and take critical business applications and move them into the cloud.
We would like to see designs that use the color blue. The final design should communicate confidence, agility and speak to technology focused customers. Forward progress and/or motion should be conveyed.

Target Market(s)

Government customers and large enterprise companies

Industry/Entity Type

Telecommunications

Font styles to use
Sans Serif

Colors
0555a3

Requirements
Must have
• different slides: Cover page, title slide, main content, transition slide, close out slide..

```html
<!DOCTYPE html>
<html lang="en">
<head>
<meta charset="utf-8">
<title>KMaldrey Consulting – Presentation Template</title>
<link rel="stylesheet" href="https://fonts.googleapis.com/css2?family=Open+Sans:ital,wght@0,400;0,600;0,700;1,700&family=Montserrat:wght@400;600&display=swap">
<style>
:root{
  --brand:#0555a3;
  --ink:#3c3c3c;
  --muted:#6b6b6b;
  --rule:#cfcfcf;
  --charcoal:#3a3a3a;
  --stage:#2c2a28;
  --white:#ffffff;
  --green:#8fb84e;
  --mid-blue:#2e80c2;
  --navy:#263a56;
}
*{box-sizing:border-box;margin:0;padding:0}
html,body{width:1000px;height:1200px;overflow:hidden}
body{background:var(--stage);font-family:"Open Sans",Arial,sans-serif;color:var(--ink);position:relative}
.slide{position:absolute;width:457px;height:342px;background:var(--white);overflow:hidden}
.s1{left:28px;top:57px}.s2{left:514px;top:57px}
.s3{left:28px;top:431px}.s4{left:514px;top:431px}
.s5{left:28px;top:802px}.s6{left:514px;top:802px}

/* company name: plain text with one square */
.company{position:absolute;display:flex;align-items:center;gap:5px;color:var(--charcoal);font-family:"Open Sans",sans-serif;font-weight:400;white-space:nowrap;line-height:1}
.company-square{width:6px;height:6px;background:var(--charcoal);flex:none}
.company-small{right:28px;bottom:20px;font-size:8px}
.company-cover{left:22px;top:44px;font-size:18px;gap:9px}
.company-cover .company-square{width:13px;height:13px}
.company-ty{right:26px;bottom:18px;font-size:12px;gap:6px}
.company-ty .company-square{width:8px;height:8px}
.s5 .company{color:var(--white)}
.s5 .company-square{background:var(--white)}

.page-bar{position:absolute;left:0;right:0;bottom:0;height:9px;background:var(--brand)}
.page-num{position:absolute;right:0;bottom:0;width:34px;height:9px;background:var(--white);clip-path:polygon(6px 0,100% 0,100% 100%,0 100%);color:var(--charcoal);font-size:6px;font-weight:700;text-align:right;padding-right:11px;line-height:9px}

.head{position:absolute;left:13px;top:4px}
.head-title{font-weight:700;font-size:17px;color:var(--brand);line-height:20px}
.head-sub{font-size:12.5px;color:var(--charcoal);line-height:14px}
.head-rule{position:absolute;left:13px;right:13px;top:41px;height:1px;background:var(--rule)}

/* cover */
.cover-band{position:absolute;left:0;right:0;top:89px;bottom:0;background:var(--brand)}
.cover-tab{position:absolute;left:0;top:86px;width:203px;height:5px;background:var(--charcoal)}
.cover-title{position:absolute;left:18px;top:164px;color:var(--white);font-family:"Montserrat",sans-serif;font-weight:600;font-size:18.5px;line-height:24px}
.cover-sub{position:absolute;left:18px;top:215px;color:var(--white);font-family:"Montserrat",sans-serif;font-size:13px}
.cover-date{position:absolute;left:18px;top:247px;color:var(--white);font-family:"Montserrat",sans-serif;font-size:13px}

/* intro */
.intro-photo{position:absolute;left:0;right:0;top:43px;height:153px;background:linear-gradient(90deg,#1d5cab 0%,#2f74c4 45%,#1c5aa8 100%)}
.intro-text{position:absolute;left:26px;right:26px;top:220px;font-size:9.6px;line-height:15px;text-align:center;color:var(--muted)}

/* text slide */
.pull-quote{position:absolute;left:18px;top:77px;width:108px;font-size:6.2px;line-height:9.4px;font-weight:700;font-style:italic;color:var(--brand);text-align:justify}
.col{position:absolute;top:77px;width:138px;font-size:6.1px;line-height:10.4px;color:var(--muted);text-align:justify}
.col p+p{margin-top:10px;text-indent:10px}
.col-a{left:146px}.col-b{left:300px}

/* charts */
.chart-bar{position:absolute;left:8px;top:85px}
.chart-pie{position:absolute;left:270px;top:90px}
.divider{position:absolute;left:234px;top:80px;width:1px;height:176px;background:#e2e2e2}
.chart-cap{position:absolute;top:212px;width:160px}
.chart-cap h3{font-weight:400;font-size:10px;color:var(--charcoal);margin-bottom:3px}
.chart-cap p{font-size:6.8px;line-height:9.4px;color:var(--muted)}

/* section */
.s5{background:linear-gradient(135deg,#2f6fbf 0%,#2566b8 50%,#1f5eb0 100%)}
.section-ring{position:absolute;left:176px;top:118px}
.section-label{position:absolute;left:176px;top:118px;width:106px;height:106px;display:flex;align-items:center;justify-content:center;text-align:center;color:var(--white);font-weight:700;font-size:14px;line-height:16px}

/* thank you */
.ty-tab{position:absolute;left:126px;top:60px;width:202px;height:4px;background:var(--charcoal)}
.ty-band{position:absolute;left:0;right:0;top:62px;height:218px;background:var(--brand)}
.ty-title{position:absolute;left:0;right:0;top:92px;text-align:center;color:var(--white);font-weight:700;font-size:34px;letter-spacing:.5px}
.contact{position:absolute;display:flex;align-items:flex-start;gap:9px;color:var(--white);font-size:10px;line-height:14px;white-space:nowrap}
.contact svg{flex:none;margin-top:1px}
.contact-wrap{white-space:normal}
.dot{width:10px;height:10px;border-radius:50%;background:var(--white);flex:none;margin-top:2px}
</style>
</head>
<body>

<!-- Cover -->
<section class="slide s1">
  <div class="company company-cover"><span class="company-square"></span><span>KMaldrey Consulting</span></div>
  <div class="cover-band"></div>
  <div class="cover-tab"></div>
  <h1 class="cover-title">Insert The Title of Your<br>Presentation Here</h1>
  <p class="cover-sub">Subtitle of the Presentation</p>
  <p class="cover-date">April 12, 2015</p>
</section>

<!-- Introduction -->
<section class="slide s2">
  <div class="head"><h2 class="head-title">INTRODUCTION</h2><p class="head-sub">About Us</p></div>
  <div class="intro-photo" role="img" aria-label="Blue-tinted photo of a business handshake over a city skyline"></div>
  <p class="intro-text">Lorem ipsum dolor sit amet, consectetur adipiscing elit, sed do eiusmod tempor incididunt ut labore et dolore magna aliqua. Ut enim ad minim veniam, quis nostrud exercitation ullamco laboris nisi ut aliquip ex ea commodo consequat. Duis aute irure dolor in reprehenderit in voluptate velit esse cillum dolore eu fugiat nulla pariatur.</p>
  <div class="company company-small"><span class="company-square"></span><span>KMaldrey Consulting</span></div>
  <div class="page-bar"></div><div class="page-num">2</div>
</section>

<!-- Text content -->
<section class="slide s3">
  <div class="head"><h2 class="head-title">YOUR SAMPLE TITLE</h2><p class="head-sub">Your subtitle goes here</p></div>
  <div class="head-rule"></div>
  <blockquote class="pull-quote">“Sed ut perspiciatis unde omnis iste natus error sit voluptatem accusantium doloremque laudantium, totam rem aperiam, eaque ipsa quae ab illo inventore veritatis et quasi architecto beatae vitae”</blockquote>
  <div class="col col-a">
    <p>Lorem ipsum dolor sit amet, consectetur adipiscing elit, sed do eiusmod tempor incididunt ut labore et dolore magna aliqua. Ut enim ad minim veniam, quis nostrud exercitation ullamco laboris nisi ut aliquip ex ea commodo consequat. Duis aute irure dolor in reprehenderit in voluptate velit esse cillum dolore eu fugiat nulla pariatur. Excepteur sint occaecat cupidatat non proident, sunt in culpa qui officia deserunt mollit anim id est laborum.</p>
    <p>Sed ut perspiciatis unde omnis iste natus error sit voluptatem accusantium doloremque laudantium, totam rem aperiam, eaque ipsa quae ab illo inventore veritatis et quasi architecto beatae vitae dicta sunt explicabo. Nemo enim ipsam voluptatem quia voluptas sit aspernatur</p>
  </div>
  <div class="col col-b">
    <p>aut odit aut fugit, sed quia consequuntur magni dolores eos qui ratione voluptatem sequi nesciunt. Neque porro quisquam est, qui dolorem ipsum quia dolor sit amet, consectetur, adipisci velit, sed quia non numquam eius modi tempora incidunt ut labore et dolore magnam aliquam quaerat voluptatem. Ut enim ad minima veniam, quis nostrum exercitationem ullam corporis suscipit laboriosam, nisi ut aliquid ex ea commodi consequatur?</p>
    <p>Quis autem vel eum iure reprehenderit qui in ea voluptate velit esse quam nihil molestiae consequatur, vel illum qui dolorem eum fugiat quo voluptas nulla pariatur? At vero eos et</p>
  </div>
  <div class="company company-small"><span class="company-square"></span><span>KMaldrey Consulting</span></div>
  <div class="page-bar"></div><div class="page-num">3</div>
</section>

<!-- Charts -->
<section class="slide s4">
  <div class="head"><h2 class="head-title">YOUR SAMPLE TITLE</h2><p class="head-sub">Your subtitle goes here</p></div>
  <div class="head-rule"></div>
  <svg class="chart-bar" width="220" height="120" viewBox="0 0 220 120" font-family="Open Sans, sans-serif" font-size="5" fill="#555">
    <g stroke="#e6e6e6" stroke-width=".6">
      <line x1="25" y1="5" x2="165" y2="5"/><line x1="25" y1="15" x2="165" y2="15"/><line x1="25" y1="25" x2="165" y2="25"/><line x1="25" y1="35" x2="165" y2="35"/><line x1="25" y1="45" x2="165" y2="45"/><line x1="25" y1="55" x2="165" y2="55"/><line x1="25" y1="65" x2="165" y2="65"/><line x1="25" y1="75" x2="165" y2="75"/><line x1="25" y1="85" x2="165" y2="85"/><line x1="25" y1="95" x2="165" y2="95"/>
    </g>
    <line x1="25" y1="105" x2="165" y2="105" stroke="#999" stroke-width=".6"/>
    <g text-anchor="end">
      <text x="20" y="7">5</text><text x="20" y="17">4.5</text><text x="20" y="27">4</text><text x="20" y="37">3.5</text><text x="20" y="47">3</text><text x="20" y="57">2.5</text><text x="20" y="67">2</text><text x="20" y="77">1.5</text><text x="20" y="87">1</text><text x="20" y="97">0.5</text><text x="20" y="107">0</text>
    </g>
    <g fill="var(--green)"><rect x="33" y="19" width="10" height="86"/><rect x="80" y="55" width="10" height="50"/><rect x="127" y="35" width="10" height="70"/></g>
    <g fill="var(--mid-blue)"><rect x="43" y="57" width="10" height="48"/><rect x="90" y="17" width="10" height="88"/><rect x="137" y="69" width="10" height="36"/></g>
    <g fill="var(--navy)"><rect x="53" y="65" width="10" height="40"/><rect x="100" y="65" width="10" height="40"/><rect x="147" y="45" width="10" height="60"/></g>
    <g text-anchor="middle"><text x="48" y="114">Category 1</text><text x="95" y="114">Category 2</text><text x="142" y="114">Category 3</text></g>
    <rect x="172" y="51" width="4" height="4" fill="var(--green)"/><text x="179" y="55">Series 1</text>
    <rect x="172" y="62" width="4" height="4" fill="var(--mid-blue)"/><text x="179" y="66">Series 2</text>
    <rect x="172" y="73" width="4" height="4" fill="var(--navy)"/><text x="179" y="77">Series 3</text>
  </svg>
  <div class="divider"></div>
  <svg class="chart-pie" width="170" height="100" viewBox="0 0 170 100" font-family="Open Sans, sans-serif" font-size="5.5" fill="#555">
    <path d="M50 50 L50 1 A49 49 0 0 1 65.1 96.6 Z" fill="var(--green)"/>
    <path d="M50 50 L65.1 96.6 A49 49 0 0 1 7.1 73.8 Z" fill="var(--mid-blue)"/>
    <path d="M50 50 L7.1 73.8 A49 49 0 0 1 50 1 Z" fill="var(--navy)"/>
    <rect x="120" y="42" width="4" height="4" fill="var(--green)"/><text x="127" y="46">Category 1</text>
    <rect x="120" y="53" width="4" height="4" fill="var(--mid-blue)"/><text x="127" y="57">Category 2</text>
    <rect x="120" y="64" width="4" height="4" fill="var(--navy)"/><text x="127" y="68">Category 3</text>
  </svg>
  <div class="chart-cap" style="left:45px"><h3>Chart Sample One</h3><p>Lorem ipsum dolor sit amet, consectetur adipiscing elit. Aliquam tincidunt ante nec sem congue convallis lorem ipsum.</p></div>
  <div class="chart-cap" style="left:272px"><h3>Chart Sample Two</h3><p>Lorem ipsum dolor sit amet, consectetur adipiscing elit. Aliquam tincidunt ante nec sem congue convallis lorem ipsum.</p></div>
  <div class="company company-small"><span class="company-square"></span><span>KMaldrey Consulting</span></div>
  <div class="page-bar"></div><div class="page-num">4</div>
</section>

<!-- Section divider -->
<section class="slide s5" role="img" aria-label="Blue-tinted photo of a laptop and a coffee mug on a desk">
  <svg class="section-ring" width="106" height="106" viewBox="0 0 106 106">
    <circle cx="53" cy="53" r="48" fill="none" stroke="#d9d9d9" stroke-width="10"/>
    <circle cx="53" cy="53" r="48" fill="none" stroke="var(--charcoal)" stroke-width="10" stroke-dasharray="75 227" transform="rotate(-90 53 53)"/>
  </svg>
  <div class="section-label">SECTION<br>TWO</div>
  <div class="company company-small"><span class="company-square"></span><span>KMaldrey Consulting</span></div>
</section>

<!-- Closing -->
<section class="slide s6">
  <div class="ty-band"></div>
  <div class="ty-tab"></div>
  <h2 class="ty-title">THANK YOU</h2>
  <div class="contact contact-wrap" style="left:20px;top:160px;width:165px">
    <svg width="10" height="12" viewBox="0 0 10 12"><path d="M5 0a4.5 4.5 0 0 0-4.5 4.5C.5 8 5 12 5 12s4.5-4 4.5-7.5A4.5 4.5 0 0 0 5 0zm0 6.3a1.8 1.8 0 1 1 0-3.6 1.8 1.8 0 0 1 0 3.6z" fill="#fff"/></svg>
    <span>Lorem ipsum dolor sit amet, consectetur adipiscing elit, sed do eiusmod tempor incididunt ut labore et dolore</span>
  </div>
  <div class="contact" style="left:20px;top:231px">
    <svg width="11" height="11" viewBox="0 0 11 11"><path d="M2.2 0.5l1.8 2.1-1 1.2c.6 1.5 1.7 2.6 3.2 3.2l1.2-1 2.1 1.8-.9 1.9C5 9.6 1.4 6 .3 1.4z" fill="#fff"/></svg>
    <span>1234567890</span>
  </div>
  <div class="contact" style="left:248px;top:161px">
    <svg width="13" height="10" viewBox="0 0 13 10"><rect x=".6" y=".6" width="11.8" height="8.8" fill="none" stroke="#fff" stroke-width="1.2"/><path d="M.6.6 6.5 5.5 12.4.6" fill="none" stroke="#fff" stroke-width="1.2"/></svg>
    <span>jhon.doe@kmaldreyconsulting.com</span>
  </div>
  <div class="contact" style="left:250px;top:189px"><span class="dot"></span><span>kmaldreyconsulting</span></div>
  <div class="contact" style="left:250px;top:217px"><span class="dot"></span><span>@kmaldreyconsulting</span></div>
  <div class="contact" style="left:250px;top:245px"><span class="dot"></span><span>www.kmaldreyconsulting.com</span></div>
  <div class="company company-ty"><span class="company-square"></span><span>KMaldrey Consulting</span></div>
</section>

</body>
</html>
```